Marrowby Cay Soda

We need an eco-label designed to go on our soda bottles that will be for sale on a tiny island off the east coast of Australia. The label is a printed card (double sided) that is 60mm wide and 180mm long. There is a 40mm by 40mm hole that is used to place on the bottle, as shown in the photos. One side is the back label, this has some regulatory requirements such as a panel of % of dietary intake, an ingredient list and a line that reads "Batch:_________". That is standard on each back panel. The front needs to have the name of the soda flavour and design of label. The reverse will need to have a blurb about us, our story and how to recycle the bottle.

We would like the design to be funny, possibly using Commodore Sir Basil Tranter's photoshopped image (he is a grizzly dude the island is named after see google images) or anything you talented people come up with.

We want to use the same format and then will need to change the name for the flavours, change the ingredients list and replace the standard box for the % daily intake.

Target Market(s)

The Product will stand next to the big soda companies that all know and thus must stand out visually from them to get the customer to have a second look at the product

Industry/Entity Type

Soda

Requirements
Must have
• Space for the Flavour on the front ie "Lemonade". "Batch:_________" at the base of the back panel.
Nice to have
• Island feel, Possibly using "Commodore Sir Tranter" holding a drink?!? Palms, sunsets

```html
<!DOCTYPE html>
<html lang="en">
<head>
<meta charset="utf-8">
<title>Marrowby Cay Soda – Eco Label</title>
<link href="https://fonts.googleapis.com/css2?family=Great+Vibes&family=Josefin+Sans:wght@300;400&family=Poiret+One&display=swap" rel="stylesheet">
<style>
  :root{
    --page:#ffffff;
    --frame:#1a1a1a;
    --ink:#111111;
    --sand-light:#f1d9a4;
    --sand:#e3bd77;
    --sand-pale:#e7d3b5;
    --turquoise:#4fd3e0;
    --sky-light:#a9dcf7;
    --sky:#4aa6ee;
    --deep-blue:#0a35d8;
    --sea:#3db6d8;
    --panel:#aad3fb;
    --brand:#1fb0e6;
    --ring:#6a8cf0;
    --flavour:#21a8c5;
  }
  *{box-sizing:border-box;margin:0;padding:0}
  html,body{width:1200px;height:847px;overflow:hidden;background:var(--page)}
  .sheet{position:relative;width:1200px;height:847px;border:1px solid var(--frame);}
  .strip{position:absolute;top:60px;width:243px;height:730px;border:1px solid #8a7a62;overflow:hidden}
  .strip--story{left:283px;
    background:linear-gradient(to bottom,
      var(--sand-light) 0,var(--sand) 55px,var(--sand-light) 85px,
      var(--turquoise) 90px,#2fc4e3 112px,var(--sky-light) 125px,
      #cfe8fb 165px,var(--sky) 250px,var(--deep-blue) 375px,
      var(--sky) 440px,var(--sky-light) 500px,#dff1fc 590px,
      var(--sea) 598px,#7dd8e6 615px,var(--sand-light) 640px,var(--sand) 730px);}
  .strip--back{left:721px;
    background:linear-gradient(to bottom,
      var(--sand-pale) 0,var(--sand-pale) 60px,var(--sea) 75px,
      #6ac7ea 150px,var(--sky-light) 260px,#8fd2f3 420px,
      #6cc5ea 530px,#2fa7c9 620px,#8ccad3 655px,var(--sand-pale) 690px,var(--sand-pale) 730px);}
  .hole{position:absolute;top:284px;left:40px;width:162px;height:162px;background:var(--page);border:1px solid #555}
  .fold{position:absolute;left:0;right:0;top:374px;height:1px;background:rgba(255,255,255,.35)}
  .flip{position:absolute;left:0;top:0;width:243px;height:280px;transform:rotate(180deg)}
  .script{font-family:"Great Vibes",cursive;color:var(--ink)}
  .recycle-title{position:absolute;left:27px;top:40px;font-size:22px;white-space:nowrap}
  .recycle-text{position:absolute;right:20px;top:92px;width:160px;text-align:left;font-size:17px;line-height:29px}
  .bottle-photo{position:absolute;left:132px;top:8px;width:95px;height:104px;
    background:linear-gradient(to bottom,#eef3f5,#c9d6dc 60%,#9fb4bd);border-radius:6px;opacity:.9}
  .history{position:absolute;left:8px;right:8px;top:485px;text-align:center;font-size:17.5px;line-height:28.8px}
  .allergen{position:absolute;left:0;right:0;top:212px;text-align:center;font-family:"Poiret One",sans-serif;font-size:18px;color:var(--ink)}
  .batch{position:absolute;left:8px;top:238px;font-family:"Poiret One",sans-serif;font-size:24px;color:var(--ink);white-space:nowrap}
  .ingredients{position:absolute;left:25px;top:17px;width:195px;height:192px;background:var(--panel);border-radius:22px;
    padding-top:9px;text-align:center;font-family:"Great Vibes",cursive;font-size:14.5px;line-height:24px;color:var(--ink)}
  .ingredients h2{font:inherit;text-decoration:underline}
  .brand{position:absolute;left:44px;top:510px;width:160px;height:160px;border-radius:50%;
    border:3px solid var(--ring);background:radial-gradient(circle,rgba(255,255,255,.75),rgba(255,255,255,.15));
    display:flex;align-items:center;justify-content:center;text-align:center}
  .brand-name{font-family:"Josefin Sans",sans-serif;font-weight:300;font-size:20px;line-height:26px;color:var(--brand);letter-spacing:1px}
  .flavour{position:absolute;right:10px;top:680px;font-family:"Great Vibes",cursive;font-size:31px;color:var(--flavour)}
</style>
</head>
<body>
<main class="sheet">
  <section class="strip strip--story">
    <div class="flip">
      <h2 class="recycle-title script">How to Recycle :-</h2>
      <p class="recycle-text script">The goli soda bottles would go back to get refilled at a factory.</p>
    </div>
    <div class="bottle-photo" role="img" aria-label="Photo of two glass marble-neck soda bottles"></div>
    <div class="fold"></div>
    <div class="hole"></div>
    <p class="history script">Designed and patented for carbonated drinks in 1872 by British swig maker Silas Thorne of Harrowgate, London, the glass bottle is specially made to encase a round marble and a rubber washer in the neck.</p>
  </section>

  <section class="strip strip--back">
    <div class="flip">
      <div class="ingredients">
        <h2>Ingredient</h2>
        <p>Purified Carbonated water</p>
        <p>Sugar</p>
        <p>Acidity Regulator (330, 331)</p>
        <p>Preservative (211)</p>
        <p>Stabilizers (414, 415)</p>
        <p>Permitted food colours</p>
        <p>Natural Flavours</p>
      </div>
      <p class="allergen">May contain Nuts etc.</p>
      <p class="batch">Batch ____________</p>
    </div>
    <div class="hole"></div>
    <div class="brand">
      <p class="brand-name">Marrowby Cay<br>Soda</p>
    </div>
    <p class="flavour">Lemonade</p>
  </section>
</main>
</body>
</html>
```